都内でエステサロンを運営されている
美容家さんの電子書籍を出版しますので、
表紙デザイン作成をお願いいたします。

ーーーーーーーーーーー
■本のタイトル
月灯集

【サブタイトル】
朝の散歩で心を整える本

<著者>沙耶(さや)

ーーーーーーーーーー

納品は、2,560 x 1,600 ピクセルのJPEGと
元データをお願い致したく。

著者プロフィール
美容家、エステティシャン

サロンのイメージカラーはピンク、白ですが
表紙デザインに色のこだわりはありません。

ーーーー

■デザイン要望

優しさ,明るさ、清潔感と品格、プロフェッショナル感があるものをお願いします。

【コンセプト】
美容ジプシー、悩める女性たちに(男性も歓迎)贈りたい
優しく楽しい小さなご褒美タイムとその作法(洗顔やお肌のお手入れに関するメソッド)を提供する

肌質はみんなそれぞれちがいますが、本当に幸せな自分磨きは毎日のスキンケア一択。その極意を惜しみなく提供。

添付に表紙イメージの参考を挙げましたが
デザイナー様のセンスにお任せします。

ーーーーーーーーーー

※その他イラストや写真等素材を使用される場合には、商用利用可の素材をお願いします。
(Pavrelにて販売予定のため)

デザインを考えるのに必要な情報などありましたら、お答えしますので、ご遠慮なくお問い合わせ下さい。

納期は予告なく短縮する場合がございます。
よろしくお願い申し上げます。

著者様のご希望優先で決定させていただきました。

美容の道を極めた想いと、透明感、躍動感、生き生きとした理想の美人像を彷彿とさせる素敵な表紙ということで、選定させていただきます。

この度は、当コンペにご提案を頂き誠にありがとうございます。
リピートのデザイナー様もいらして、どれも素晴らしく貴重なお時間と労力を割いてくださって
本当にありがとうございました。心より感謝申し上げます。

今回選定できなかった方々の作品も大切に拝見し、個別に依頼できそうな案件などありましたらご紹介させていただきます。みなさまのご活躍祈念しております。

これからも大切に作品を制作してまいります。
どうぞまたコンペ開催の際にはご縁をいただけましたら幸いです。

本当にどうもありがとうございました。

```html
<!DOCTYPE html>
<html lang="ja">
<head>
<meta charset="UTF-8">
<title>月灯集 — 沙耶 著</title>
<link rel="stylesheet" href="https://fonts.googleapis.com/css2?family=Noto+Serif+JP:wght@300;400;500;600&family=Shippori+Mincho:wght@500;600&display=swap">
<style>
  :root {
    --photo-top: #3e2f29;
    --photo-upper: #7a655a;
    --photo-mid: #9f8c80;
    --photo-lower: #cfc6bf;
    --photo-bottom: #e8e4e0;
    --ink-white: #ffffff;
    --accent-red: #e2363a;
    --ink-dark: #2a211d;
  }
  html, body {
    margin: 0;
    padding: 0;
    width: 750px;
    height: 1200px;
    overflow: hidden;
    background: var(--photo-bottom);
  }
  .cover {
    position: relative;
    width: 750px;
    height: 1200px;
    overflow: hidden;
    font-family: "Noto Serif JP", "Shippori Mincho", serif;
  }
  .cover-photo {
    position: absolute;
    inset: 0;
    background: linear-gradient(180deg,
      var(--photo-top) 0%,
      var(--photo-upper) 28%,
      var(--photo-mid) 52%,
      var(--photo-lower) 80%,
      var(--photo-bottom) 100%);
  }
  .tagline {
    position: absolute;
    top: 165px;
    left: 250px;
    margin: 0;
    color: var(--ink-white);
    font-family: "Shippori Mincho", serif;
    font-weight: 500;
    font-size: 26px;
    line-height: 46px;
    letter-spacing: 0.02em;
    text-shadow: 0 1px 5px rgba(0,0,0,0.3);
  }
  .tagline span { display: block; }
  .tagline .second { padding-left: 62px; }
  .title {
    position: absolute;
    top: 452px;
    left: 0;
    width: 750px;
    margin: 0;
    text-align: center;
    font-weight: 300;
    font-size: 218px;
    line-height: 1;
    letter-spacing: 0.04em;
    color: var(--accent-red);
  }
  .title .lead { color: var(--ink-white); }
  .subtitle {
    position: absolute;
    top: 716px;
    left: 350px;
    width: 300px;
    margin: 0;
    text-align: center;
    color: var(--ink-white);
    font-family: "Shippori Mincho", serif;
    font-weight: 600;
    font-size: 33px;
    line-height: 52px;
    text-shadow: 0 1px 5px rgba(0,0,0,0.25);
  }
  .subtitle span { display: block; }
  .author {
    position: absolute;
    top: 1078px;
    left: 0;
    width: 750px;
    margin: 0;
    text-align: center;
    color: var(--ink-dark);
    font-weight: 600;
    font-size: 44px;
    line-height: 1;
  }
  .author .reading {
    font-size: 18px;
    font-weight: 500;
    margin: 0 14px 0 6px;
    vertical-align: -4px;
  }
</style>
</head>
<body>
  <main class="cover">
    <div class="cover-photo" role="img" aria-label="黒髪の女性のポートレートと赤いガーベラの花の写真"></div>

    <p class="tagline">
      <span>迷える美容ジプシーよ、</span>
      <span class="second">これが救いだ</span>
    </p>

    <h1 class="title"><span class="lead">月</span>灯集</h1>

    <p class="subtitle">
      <span>朝の散歩で</span>
      <span>心を整える本</span>
    </p>

    <p class="author">沙耶<span class="reading">さや</span>著</p>
  </main>
</body>
</html>
```